Lower-middle market private equity firm needs its PowerPoint template update/refresh

Wexford Lindqvist Capital Partners is a lower-middle market private equity firm focused on acquiring family- and founder-owned businesses in the industrial market. Website is here for more info: https://www.wlcpx-example.com/. We would like to upgrade/update our powerpoint template/slide master we use for marketing materials - uploading a powerpoint version with some of the slide templates we use. We would like to keep it classic and clean with a white background and color on top and enough room for text on the pages. We would prefer to stay within the color palette of the hash tag logo on the cover page (cover page needs an update as well). We are open to suggestions on the font we utilize as well.

```html
<!DOCTYPE html>
<html lang="en">
<head>
<meta charset="utf-8">
<title>Wexford Lindqvist Capital Partners – Slide Template</title>
<link href="https://fonts.googleapis.com/css2?family=Montserrat:wght@400;500;600;700&family=Playfair+Display:wght@700&display=swap" rel="stylesheet">
<style>
:root{
  --page:#e8e9ea;
  --slide:#ffffff;
  --panel:#e6e7e6;
  --ink:#3b3b3b;
  --ink-soft:#6a6a6a;
  --brand-name:#8a7e70;
  --green:#1b9a4a;
  --chevron:#3e8a45;
  --lavender:#9ea6cf;
  --sky:#8fc3e8;
  --olive:#c4b400;
  --lime:#d4dc1c;
}
*{margin:0;padding:0;box-sizing:border-box}
html,body{width:1200px;height:969px;overflow:hidden;background:var(--page)}
body{position:relative;font-family:"Montserrat",sans-serif;color:var(--ink)}
.slide{position:absolute;width:539px;height:404px;background:var(--slide)}
.slide--cover{left:46px;top:64px}
.slide--team{left:616px;top:64px}
.slide--section{left:46px;top:502px}
.slide--grid{left:616px;top:502px}

.slide-title{position:absolute;left:23px;top:17px;font-family:"Playfair Display",serif;font-weight:700;font-size:30px;color:var(--ink);line-height:1.2}

.brand{position:absolute;display:flex;align-items:center;gap:6px}
.brand__mark{width:10px;height:10px;background:var(--green);flex:none}
.brand__name{font-weight:700;color:var(--brand-name);text-transform:uppercase;line-height:1.15}
.brand--corner{right:22px;top:22px}
.brand--corner .brand__name{font-size:6px;width:40px}
.brand--cover{left:22px;top:22px;gap:12px}
.brand--cover .brand__mark{width:44px;height:44px}
.brand--cover .brand__name{font-size:10.5px;line-height:1.3}

.footer{position:absolute;left:22px;top:352px;width:495px;height:29px;background:var(--panel);font-size:7.5px;display:flex;align-items:center}
.footer__mark{position:absolute;left:7px;top:8px;width:13px;height:13px;background:var(--green)}
.footer__text{position:absolute;left:45px}
.footer__page{position:absolute;right:24px}
.slide--cover .footer__mark{left:auto;right:7px}
.slide--cover .footer__text{left:22px}

/* cover */
.hero{position:absolute;left:22px;top:109px;width:495px;height:187px;overflow:hidden;
  background:
   radial-gradient(ellipse 90px 160px at 200px 110px,rgba(120,200,230,.85),transparent 70%),
   radial-gradient(ellipse 160px 140px at 420px 120px,rgba(110,60,140,.8),transparent 70%),
   linear-gradient(100deg,#1d3470 0%,#23457a 30%,#2a3c78 60%,#4a3a80 100%)}
.hero__panel{position:absolute;left:24px;top:30px;width:446px;height:101px;background:rgba(20,60,50,.55)}
.hero__headline{position:absolute;left:45px;top:45px;font-family:"Playfair Display",serif;font-weight:700;font-size:28.5px;line-height:1.1;color:#fff;text-shadow:0 2px 4px rgba(0,0,0,.5)}
.values{position:absolute;left:44px;top:143px;display:flex;gap:7px}
.value{height:14.5px;padding:0 8px;font-size:6.6px;color:#fff;display:flex;align-items:center;text-transform:uppercase}
.value--lavender{background:var(--lavender);width:71px}
.value--green{background:var(--green);width:56px}
.value--sky{background:var(--sky);width:72px}
.value--olive{background:var(--olive);width:49px}
.cover-meta{position:absolute;right:67px;top:308px;text-align:right}
.cover-meta__url{font-size:8.5px}
.cover-meta__date{font-size:12.5px;font-weight:700;margin-top:1px}

/* team */
.group-label{position:absolute;left:23px;font-size:12.5px;font-weight:500}
.people{position:absolute;left:23px;display:flex;gap:6px}
.person{width:88px;height:93px;background:#fff;box-shadow:0 1px 4px rgba(0,0,0,.18)}
.person__photo{height:59px;background:linear-gradient(180deg,#8d8e8c 0%,#5d6066 55%,#2f3a52 100%)}
.person__name{font-size:8.5px;font-weight:600;margin:8px 0 0 6px}
.person__role{font-size:5.8px;color:var(--ink-soft);margin:1px 0 0 6px}
.side-list{position:absolute;left:404px;top:71px;width:113px;height:262px;background:var(--panel);padding-top:8px}

.bullets{list-style:none}
.bullets li{position:relative;font-size:8.8px;padding-left:25px;height:21px;line-height:21px}
.bullets li::before{content:"";position:absolute;left:9px;top:8.5px;width:3.5px;height:3.5px;border-top:1.5px solid var(--chevron);border-right:1.5px solid var(--chevron);transform:rotate(45deg)}

/* section */
.content-area{position:absolute;left:22px;top:71px;width:495px;height:262px;background:var(--panel)}

/* grid */
.card{position:absolute;width:241px;height:125px;background:var(--panel);overflow:hidden}
.card--a{left:23px;top:71px}
.card--b{left:275px;top:71px}
.card--c{left:23px;top:208px}
.card--d{left:275px;top:208px}
.card__corner{position:absolute;right:0;top:0;width:0;height:0;border-style:solid;border-width:0 16px 16px 0}
.card--a .card__corner{border-color:transparent var(--sky) transparent transparent}
.card--b .card__corner{border-color:transparent var(--green) transparent transparent}
.card--c .card__corner{border-color:transparent var(--lavender) transparent transparent}
.card--d .card__corner{border-color:transparent var(--lime) transparent transparent}
.card__title{position:absolute;left:11px;top:6px;font-size:13px}
.card .bullets{position:absolute;left:-2px;top:25px}
.card .bullets li{height:16.5px;line-height:16.5px;padding-left:27px}
.card .bullets li::before{top:6.5px;left:11px}
</style>
</head>
<body>

<section class="slide slide--cover">
  <div class="brand brand--cover">
    <span class="brand__mark"></span>
    <span class="brand__name">Wexford<br>Lindqvist<br>Capital<br>Partners</span>
  </div>
  <div class="hero" role="img" aria-label="Abstract blurred photograph in navy, teal and violet tones">
    <div class="hero__panel"></div>
    <h1 class="hero__headline">Realizing the promise<br>in small companies for decades</h1>
    <div class="values">
      <span class="value value--lavender">Perseverance</span>
      <span class="value value--green">Ingenuity</span>
      <span class="value value--sky">Transparency</span>
      <span class="value value--olive">Results</span>
    </div>
  </div>
  <div class="cover-meta">
    <p class="cover-meta__url">www.wlcpx-example.com</p>
    <p class="cover-meta__date">[May 2026]</p>
  </div>
  <footer class="footer">
    <span class="footer__text">WEXFORD LINDQVIST CAPITAL PARTNERS | Confidential | wlcpx-example.com</span>
    <span class="footer__mark"></span>
  </footer>
</section>

<section class="slide slide--team">
  <h2 class="slide-title">Team</h2>
  <div class="brand brand--corner"><span class="brand__mark"></span><span class="brand__name">Wexford Lindqvist Capital Partners</span></div>
  <p class="group-label" style="top:76px">Investment Professionals</p>
  <div class="people" style="top:101px">
    <article class="person"><div class="person__photo" role="img" aria-label="Portrait of Martin R. Callow"></div><p class="person__name">Martin R. Callow</p><p class="person__role">Managing Partner</p></article>
    <article class="person"><div class="person__photo" role="img" aria-label="Portrait of Oliver T. Hayne"></div><p class="person__name">Oliver T. Hayne</p><p class="person__role">Partner</p></article>
    <article class="person"><div class="person__photo" role="img" aria-label="Portrait of Daniel K. M"></div><p class="person__name">Daniel K. M</p><p class="person__role">Partner</p></article>
    <article class="person"><div class="person__photo" role="img" aria-label="Portrait of Peter W. S"></div><p class="person__name">Peter W. S</p><p class="person__role">Partner</p></article>
  </div>
  <p class="group-label" style="top:216px">Operations Professionals</p>
  <div class="people" style="top:239px">
    <article class="person"><div class="person__photo" role="img" aria-label="Portrait of L. Henrik Vale"></div><p class="person__name">L. Henrik Vale</p><p class="person__role">Chief Financial Officer</p></article>
    <article class="person"><div class="person__photo" role="img" aria-label="Portrait of Thomas J. F"></div><p class="person__name">Thomas J. F</p><p class="person__role">Managing Director</p></article>
    <article class="person"><div class="person__photo" role="img" aria-label="Portrait of Edward N. Callow"></div><p class="person__name">Edward N. Callow</p><p class="person__role">Vice President</p></article>
  </div>
  <aside class="side-list">
    <ul class="bullets"><li>Lorem ipsum</li><li>Lorem ipsum</li><li>Lorem ipsum</li><li>Lorem ipsum</li><li>Lorem ipsum</li><li>Lorem ipsum</li></ul>
  </aside>
  <footer class="footer"><span class="footer__mark"></span><span class="footer__text">WEXFORD LINDQVIST CAPITAL PARTNERS | Confidential | wlcpx-example.com</span><span class="footer__page">02</span></footer>
</section>

<section class="slide slide--section">
  <h2 class="slide-title" style="left:22px">New section</h2>
  <div class="brand brand--corner"><span class="brand__mark"></span><span class="brand__name">Wexford Lindqvist Capital Partners</span></div>
  <div class="content-area"></div>
  <footer class="footer"><span class="footer__mark"></span><span class="footer__text">WEXFORD LINDQVIST CAPITAL PARTNERS | Confidential | wlcpx-example.com</span><span class="footer__page">02</span></footer>
</section>

<section class="slide slide--grid">
  <h2 class="slide-title">(Tittle)</h2>
  <div class="brand brand--corner"><span class="brand__mark"></span><span class="brand__name">Wexford Lindqvist Capital Partners</span></div>
  <div class="card card--a"><span class="card__corner"></span><h3 class="card__title">Section</h3><ul class="bullets"><li>Lorem ipsum</li><li>Lorem ipsum</li></ul></div>
  <div class="card card--b"><span class="card__corner"></span><h3 class="card__title">Section</h3><ul class="bullets"><li>Lorem ipsum</li><li>Lorem ipsum</li></ul></div>
  <div class="card card--c"><span class="card__corner"></span><h3 class="card__title">Section</h3><ul class="bullets"><li>Lorem ipsum</li><li>Lorem ipsum</li></ul></div>
  <div class="card card--d"><span class="card__corner"></span><h3 class="card__title">Section</h3><ul class="bullets"><li>Lorem ipsum</li><li>Lorem ipsum</li></ul></div>
  <footer class="footer"><span class="footer__mark"></span><span class="footer__text">WEXFORD LINDQVIST CAPITAL PARTNERS | Confidential | wlcpx-example.com</span><span class="footer__page">02</span></footer>
</section>

</body>
</html>
```